Flyer Design For Building & Decorating Company

We need an A6 double-sided colour flyer for a letter-box marketing campaign. We are a building and decorating company based in West London. We saw a flyer that we liked and have attached it as an example of the sort of thing we're looking for (see attached files Example A6 Flyer - Front.png and Example A6 Flyer - Back.png). Please note that we're not expecting the designer to slavishly follow this design, more to use it as a jumping-off point.

The design must incorporate a strong call to action, e.g., Call Us For A Free, No-Obligation Quote.

The textual information that must be included in the flyer (contact methods, tagline, services, etc.) are included in the attached file Flyer Text.docx.

Also included as attachments are a selection of images used on our website (files bathroom.png, carpentry.png, decorating.jpg,
flooring.jpg, painting_decorating.jpg, repointing.jpg and work_ on_scaffold.jpg). Please include these images on the flyer (at least one image on each side), or use stock images if any of these are unsuitable.

The company logo will also need to be included in the flyer - see attached file logo.png

The images on our website have all had to be re-sized from the originals. I've attached a number of the original images to this brief, as these are the highest resolution versions of the images that we have. I would ask that you use the versions attached to the brief, but if you feel that other images from our website would work better on your flyer design, please let me know and I'll attach them to this brief.

Finally, we've attached guideline notes from our printer (see attached file Printer's Requirements.docx) - please ensure these are adhered to where relevant.

Target Market(s)

People in West London who require building or decorating work to be done on their properties.

Industry/Entity Type

Marketing

Requirements
Must have
• A6 double-sided colour flyer using the text we provided and some of the images provided.

The call to action must be prominent and eye-catching, as the only purpose of the flyer is to get recipients to contact our company for a quote.

```html
<!DOCTYPE html>
<html lang="en">
<head>
<meta charset="utf-8">
<title>H&amp;V Renovations – A6 Flyer</title>
<link rel="stylesheet" href="https://fonts.googleapis.com/css2?family=Open+Sans:ital,wght@0,400;0,600;0,700;0,800;1,400&display=swap">
<style>
:root{
  --page:#eef1f4;
  --white:#ffffff;
  --navy:#1c2a4d;
  --blue:#1aa3e0;
  --blue-dark:#0f86c4;
  --sky:#bfe4f6;
  --ink:#1b1b1b;
  --photo-bath:#3f6f9e;
  --photo-light:#cfd9e2;
}
*{box-sizing:border-box;margin:0;padding:0}
html,body{width:1200px;height:858px;overflow:hidden;background:var(--page);font-family:"Open Sans",Arial,sans-serif;color:var(--ink)}
.canvas{position:relative;width:1200px;height:858px}
.side{position:absolute;top:20px;height:818px;background:var(--white);overflow:hidden;box-shadow:0 1px 4px rgba(0,0,0,.15)}
.front{left:10px;width:572px}
.back{left:600px;width:590px}

/* front */
.front-photo{position:absolute;left:0;top:0;width:572px;height:500px;
  background:linear-gradient(160deg,#e9f4fb 0%,#b7d6ea 28%,var(--photo-bath) 55%,#2f5a86 75%,var(--photo-light) 100%)}
.front-head{position:absolute;left:22px;top:18px;color:var(--navy);font-weight:700;font-size:15px;line-height:1.3}
.brand{position:absolute;left:340px;top:112px;display:flex;flex-direction:column;align-items:center;gap:8px;
  font-weight:800;font-size:22px;line-height:1.1;color:var(--navy);text-align:center}
.brand-square{width:22px;height:22px;background:var(--navy)}
.front-band{position:absolute;left:0;top:480px;width:572px;height:338px}
.services-tab{position:absolute;left:0;top:512px;width:228px;height:36px;background:var(--navy);
  color:var(--white);font-weight:700;font-size:19px;padding:4px 0 0 14px;border-top:2px solid var(--white);border-bottom:2px solid var(--white)}
.services{position:absolute;left:16px;top:562px;list-style:none;color:var(--white);font-size:15.5px;line-height:22.5px}
.cta{position:absolute;left:292px;top:588px;width:270px;text-align:center;color:var(--white)}
.cta-lead{font-weight:700;font-size:20px}
.cta-phone{font-weight:800;font-size:30px;line-height:1.2;margin-top:2px}
.cta-line{font-weight:700;font-size:17px;line-height:1.3}

/* back */
.lists{position:absolute;left:22px;top:14px;width:260px}
.group{margin-bottom:14px}
.group h3{font-size:14.5px;font-weight:700;color:var(--navy);line-height:19px}
.group ul{list-style:none}
.group li{font-size:14px;line-height:19px;padding-left:14px;position:relative}
.group li::before{content:"";position:absolute;left:2px;top:7px;width:6px;height:6px;border-radius:50%;background:var(--ink)}
.photos{position:absolute;left:285px;top:10px;width:148px}
.photo{width:148px;margin-bottom:8px}
.p1{height:112px;background:linear-gradient(135deg,#e8e4de,#b9b2a7)}
.p2{height:118px;background:linear-gradient(135deg,#f1efea,#d5cfc4)}
.p3{height:124px;background:linear-gradient(135deg,#e6c9a6,#b88a5c)}
.p4{height:118px;background:linear-gradient(135deg,#b5573e,#8a3b29)}
.testimonial{position:absolute;left:444px;top:12px;width:140px;font-size:10.6px;line-height:13.8px;color:var(--ink)}
.testimonial .quote-mark{font-size:26px;font-weight:800;line-height:10px;vertical-align:-10px;color:var(--navy)}
.testimonial cite{font-style:normal;display:block}
.quote-box{position:absolute;left:285px;top:532px;width:295px;height:40px;border:1.5px solid var(--ink);
  text-align:center;font-weight:800;font-size:21px;line-height:37px;color:var(--ink)}
.back-wave{position:absolute;left:0;top:580px}
.address{position:absolute;left:22px;top:728px;color:var(--white);font-size:11.5px;line-height:15px}
.address strong{font-weight:700}
.find-out{position:absolute;left:352px;top:612px;width:230px;color:var(--navy);font-weight:700;font-size:19px;line-height:24px}
</style>
</head>
<body>
<div class="canvas">

  <section class="side front">
    <div class="front-photo" role="img" aria-label="Photo of a renovated bathroom with blue panelled wall, bath and radiator"></div>
    <p class="front-head">West London Builders &amp; Decorators<br>Quality Renovations At Affordable Prices</p>
    <div class="brand"><span class="brand-square"></span>H&amp;V<br>Renovations</div>

    <svg class="front-band" viewBox="0 0 572 338" width="572" height="338" aria-hidden="true">
      <path d="M0 30 C140 0 400 10 572 22 L572 338 L0 338 Z" fill="var(--blue)"/>
      <path d="M0 22 C140 -6 400 4 572 14 L572 22 C400 10 140 0 0 30 Z" fill="var(--sky)"/>
    </svg>

    <div class="services-tab">Our services</div>
    <ul class="services">
      <li>Bathrooms/Kitchens</li>
      <li>Tiling</li>
      <li>Painting/Decorating</li>
      <li>Plastering</li>
      <li>Carpentry</li>
      <li>Flooring</li>
      <li>Plumbing</li>
      <li>Electrical Works</li>
      <li>Brickwork</li>
      <li>General Repairs</li>
    </ul>

    <div class="cta">
      <p class="cta-lead">CALL US FOR A FREE</p>
      <p class="cta-phone">0208 555 0142</p>
      <p class="cta-line">contact@hv-renovations.co.uk</p>
      <p class="cta-line">www.hv-renovations.co.uk</p>
    </div>
  </section>

  <section class="side back">
    <div class="lists">
      <div class="group">
        <h3>Bathroom/Kitchen:</h3>
        <ul>
          <li>Complete/Partial Fixings</li>
          <li>Tiling</li>
          <li>Sink/Bath/Radiator</li>
          <li>Tap Repairs/Replace</li>
          <li>Fit Washing Machine/ Dishwasher</li>
        </ul>
      </div>
      <div class="group">
        <h3>Decorating:</h3>
        <ul>
          <li>Complete/Partial Works</li>
          <li>Lining/Wallpaper</li>
          <li>Painting Inside/Outside</li>
          <li>Plastering/Skimming</li>
          <li>Rectify Damage/ Freshen Paintwork</li>
        </ul>
      </div>
      <div class="group">
        <h3>Carpentry:</h3>
        <ul>
          <li>Wardrobes/Cupboards</li>
          <li>Shelving/Skirting</li>
          <li>Doors/Windows</li>
          <li>Kitchen/Bathroom Suites</li>
          <li>Wooden Floor/Laminate</li>
        </ul>
      </div>
      <div class="group">
        <h3>Maintenance/Repairs:</h3>
        <ul>
          <li>Reseal Bath/Shower</li>
          <li>Fit Shelves</li>
          <li>Electrics - Complete/Partial</li>
          <li>Sash/Gutter/Roof Repairs</li>
          <li>Lots more ...</li>
        </ul>
      </div>
      <div class="group">
        <h3>Landscaping/Roof/<br>Work On High Ladders:</h3>
        <ul>
          <li>Fencing/Paving/Decking</li>
          <li>Work On High Ladders/Scaffold</li>
          <li>Tree Cutting/Removal</li>
          <li>Roofing - New/Repair</li>
        </ul>
      </div>
    </div>

    <div class="photos">
      <div class="photo p1" role="img" aria-label="Photo of a freshly fitted kitchen"></div>
      <div class="photo p2" role="img" aria-label="Photo of decorative plaster mouldings on a ceiling"></div>
      <div class="photo p3" role="img" aria-label="Photo of a carpenter laying wooden flooring"></div>
      <div class="photo p4" role="img" aria-label="Photo of repointed red brickwork"></div>
    </div>

    <blockquote class="testimonial">
      <span class="quote-mark">&ldquo;</span>Thank come to the rescue after my first builder walked off site. He was unfazed by the scope of work required - new kitchen, bathrooms, patio, new fireplace, a host of minor internal and external repairs, and total redecoration. His team began immediately, worked a minimum 8hr day (sometimes 12!!), were punctual, polite &amp; thoroughly pleasant to have around the house, and completed the project to my entire satisfaction. There was nothing I could fault because if any problems cropped up during the job they were attended to, without complaint, at once. After 40 years experience as a Chartered Surveyor this is the best service I have ever encountered from a local builder.&rdquo;
      <cite>Daniel R., Ealing</cite>
    </blockquote>

    <div class="quote-box">No Obligation Quote</div>

    <svg class="back-wave" viewBox="0 0 590 238" width="590" height="238" aria-hidden="true">
      <path d="M0 140 C200 150 300 90 340 20 L590 20 L590 238 L0 238 Z" fill="var(--sky)"/>
      <path d="M0 148 C210 160 310 100 350 28 L590 28 L590 238 L0 238 Z" fill="var(--blue)"/>
    </svg>

    <p class="address">
      <strong>H&amp;V Renovations</strong><br>
      14 Linden Road, Ealing, London W5 0AA<br>
      Tel: 0208 555 0142, Mobile: 07700 900318<br>
      Email: contact@hv-renovations.co.uk<br>
      Web: www.hv-renovations.co.uk
    </p>

    <p class="find-out">Find Out<br>How We Can Help With Your Building And Decorating Needs</p>
  </section>

</div>
</body>
</html>
```